Need 4 Page Brush Catalogue Redesign ASAP i will sellect any one.

I have attached my existing design please do the redesign with best look.

We are an industrial brush distributor in Texas. We provide high grade brushes to the rubber, metalwork, welding/pipeline, automotive, aerospace and other industries. So, if you are looking for one of the top-rated brass wire brushes suppliers, a wire wheel brush supplier, or any other kind of brush supplier in Texas, make us your choice!

Our brushes are manufactured using high quality raw materials and are appreciated for corrosion resistance, accurate dimensions, easy installation, smooth finish, long service life and sturdy design. The best part about our brushes is that they are stringently tested by our quality controller on different parameters.

Corlow Bristle has a reputation for flexibility, innovation and the ability to react to the needs of customers quickly. Having about 25 years of experience in this industry gives us an insight into the objectives and challenges of different projects and the ability of recommending the best solution for your application.

Get in touch with us today for finding out how we can help you with brush supplies for your business.
please check the link http://www.corlowbristle.example/

Please use attached logo at your design. Added Monday, June 12, 2017

Target Market(s)

brush industry reseller

Industry/Entity Type

Industrial

Font styles to use
Serif
Sans Serif

Colors

Designer to choose colors to be used in the design.

Requirements
Must have
• creative and i catchy
Nice to have
• must be creative
Should not have
• don't use clip art

```html
<!DOCTYPE html>
<html lang="en">
<head>
<meta charset="utf-8">
<title>Corlow Bristle – Brush Catalogue Cover Spread</title>
<link rel="stylesheet" href="https://fonts.googleapis.com/css2?family=Montserrat:wght@700;800&family=Roboto:wght@400;500;700&display=swap">
<style>
  :root{
    --blue:#3f86de;
    --blue-deep:#2f6fc4;
    --green:#8cc23f;
    --green-light:#a4d04f;
    --paper:#f4f5f7;
    --tile:#e6e8ec;
    --ink:#2b2d33;
    --ink-soft:#4a4d55;
    --white:#ffffff;
    --stage:#2e2e30;
  }
  *{margin:0;padding:0;box-sizing:border-box}
  html,body{width:1200px;height:789px;overflow:hidden;background:var(--stage)}
  body{font-family:"Roboto",Arial,sans-serif;color:var(--ink)}
  .spread{position:absolute;left:80px;top:45px;width:1040px;height:700px;display:flex;box-shadow:0 10px 30px rgba(0,0,0,.45)}
  .page{position:relative;width:520px;height:700px;overflow:hidden;background:var(--paper)}
  .page svg.shapes{position:absolute;inset:0;width:520px;height:700px}
  .photo{position:absolute;border-radius:2px}

  /* back cover */
  .about{position:absolute;left:250px;top:40px;width:250px;color:var(--white);font-size:10.5px;line-height:1.45;text-align:right}
  .about strong{font-weight:700}
  .photo--paint-brushes{left:60px;top:250px;width:230px;height:230px;background:linear-gradient(135deg,#eceef1,#d5d8dd)}
  .contact{position:absolute;right:30px;top:360px;width:300px;text-align:right}
  .contact__lead{font-size:16px;line-height:1.3;color:var(--ink)}
  .contact__lead b{color:var(--blue);font-weight:700}
  .brand-name{font-family:"Roboto",Arial,sans-serif;font-weight:400;letter-spacing:.5px;color:var(--ink)}
  .contact .brand-name{font-size:22px;margin-top:16px}
  .contact__web{font-size:9.5px;font-weight:700;letter-spacing:.5px;color:var(--ink)}
  .contact__list{list-style:none;margin-top:12px;font-size:11.5px;line-height:1.55;color:var(--ink-soft)}
  .contact__list svg{width:10px;height:10px;vertical-align:-1px;margin-right:4px}

  /* front cover */
  .photo--wire-wheels{left:150px;top:15px;width:220px;height:140px;background:radial-gradient(circle at 35% 50%,#5b5d61 0,#8f8a7a 35%,#e9eaed 70%)}
  .photo--tube-brushes{left:20px;top:170px;width:170px;height:130px;background:linear-gradient(135deg,#eceef1,#b9a77b 50%,#eceef1)}
  .photo--nylon-wheel{left:200px;top:165px;width:160px;height:150px;background:radial-gradient(circle,#e9e6dc 0,#c8a45a 14%,#1f2024 22%,#2d2f34 45%,#eef0f2 50%)}
  .photo--cup-brush{left:20px;top:320px;width:150px;height:130px;background:radial-gradient(ellipse at 50% 55%,#5f6168 0,#8a8c92 35%,#eceef1 65%)}
  .headline{position:absolute;right:30px;top:360px;width:220px;text-align:right;color:var(--white);font-family:"Montserrat",Arial,sans-serif;font-weight:800;text-transform:uppercase}
  .headline span{display:block}
  .headline__top{font-size:25px;line-height:28px}
  .headline__mid{font-size:15px;font-weight:700;line-height:18px}
  .headline__end{font-size:25px;line-height:28px}
  .front-brand{position:absolute;right:30px;top:468px;text-align:right}
  .front-brand .brand-name{font-size:30px;line-height:36px}
  .front-brand .web{font-family:"Montserrat",Arial,sans-serif;font-size:13px;font-weight:800;color:var(--ink);letter-spacing:.5px}
  .phone-band{position:absolute;right:30px;top:612px;color:var(--white);font-family:"Montserrat",Arial,sans-serif;font-weight:700;font-size:17px;display:flex;align-items:center;gap:8px}
  .phone-band svg{width:16px;height:16px}
</style>
</head>
<body>
<main class="spread">
  <section class="page page--back">
    <svg class="shapes" viewBox="0 0 520 700" aria-hidden="true">
      <polygon points="0,220 260,0 520,0 520,700 0,700" fill="#eceef1"/>
      <polygon points="80,430 260,250 440,430 260,610" fill="#e4e7eb"/>
      <polygon points="0,0 520,0 520,200 0,90" fill="var(--blue)"/>
      <polygon points="220,0 520,0 520,200 380,170" fill="var(--blue-deep)" opacity=".35"/>
      <polygon points="0,520 0,700 330,700" fill="var(--blue)"/>
    </svg>
    <p class="about">Corlow Bristle has a reputation for flexibility, innovation and the ability to react to the needs of customers quickly. <strong>Having about 25 years of experience</strong> in this industry gives us an insight into the objectives and challenges of different projects and the ability of recommending the best solution for your application.</p>
    <div class="photo photo--paint-brushes" role="img" aria-label="Photo of a paint brush and a yellow scrub brush"></div>
    <div class="contact">
      <p class="contact__lead"><b>Get in touch<br>with us today</b> for finding out how we can<br>help you with brush supplies<br>for your business.</p>
      <p class="brand-name">CORLOWBRISTLE</p>
      <p class="contact__web">WWW.CORLOWBRISTLE.EXAMPLE</p>
      <ul class="contact__list">
        <li><svg viewBox="0 0 16 16"><path d="M4 1l3 3-2 2c1 2 3 4 5 5l2-2 3 3-2 3C7 15 1 9 1 3z" fill="var(--green)"/></svg>210-555-0148</li>
        <li><svg viewBox="0 0 16 16"><path d="M8 1a5 5 0 0 1 5 5c0 4-5 9-5 9S3 10 3 6a5 5 0 0 1 5-5z" fill="var(--green)"/><circle cx="8" cy="6" r="2" fill="#fff"/></svg>Dana Whitcomb 1820 mesquite hollow<br>san antonio, TX 78250 United States</li>
        <li><svg viewBox="0 0 16 16"><rect x="1" y="3" width="14" height="10" fill="none" stroke="var(--green)" stroke-width="1.5"/><path d="M1 3l7 6 7-6" fill="none" stroke="var(--green)" stroke-width="1.5"/></svg>dana.whitcomb@mail.example</li>
      </ul>
    </div>
  </section>

  <section class="page page--front">
    <svg class="shapes" viewBox="0 0 520 700" aria-hidden="true">
      <polygon points="0,0 200,0 0,200" fill="#eceef1"/>
      <polygon points="40,170 150,280 40,390 -70,280" fill="var(--green)"/>
      <polygon points="40,170 150,280 100,330 -10,220" fill="var(--green-light)" opacity=".6"/>
      <polygon points="380,0 520,0 520,80" fill="var(--blue)"/>
      <polygon points="440,190 520,240 520,700 250,700 90,540" fill="var(--green)"/>
      <polygon points="440,190 520,240 520,380 370,260" fill="var(--green-light)" opacity=".5"/>
      <polygon points="250,640 520,590 520,635 280,690" fill="var(--blue)"/>
    </svg>
    <div class="photo photo--wire-wheels" role="img" aria-label="Photo of steel and brass wire wheel brushes"></div>
    <div class="photo photo--tube-brushes" role="img" aria-label="Photo of twisted wire tube brushes"></div>
    <div class="photo photo--nylon-wheel" role="img" aria-label="Photo of a black abrasive nylon wheel brush"></div>
    <div class="photo photo--cup-brush" role="img" aria-label="Photo of a knotted wire cup brush"></div>
    <h1 class="headline">
      <span class="headline__top">Top – Rated</span>
      <span class="headline__mid">Industrial Brush</span>
      <span class="headline__mid">Distributor in</span>
      <span class="headline__end">Texas</span>
    </h1>
    <div class="front-brand">
      <p class="brand-name">CORLOWBRISTLE</p>
      <p class="web">WWW.CORLOWBRISTLE.EXAMPLE</p>
    </div>
    <p class="phone-band"><svg viewBox="0 0 16 16"><circle cx="8" cy="8" r="7" fill="none" stroke="#fff" stroke-width="1.3"/><path d="M5.5 4l1.5 1.5-1 1c.6 1.2 1.5 2.1 2.6 2.6l1-1L11 9.6l-1 1.4C7.5 10.8 5 8.3 4.6 5.4z" fill="#fff"/></svg>210-555-0148</p>
  </section>
</main>
</body>
</html>
```